Design for a Service-Based Estimate

We want a design for an Estimate that will always be sent in PDF format. The estimate or proposal is a critical document that needs to plainly show the service items, item description but also needs to be attractive and professional looking. Our current estimate deliverable is attached but it looks really basic like a Word document

```html
<!DOCTYPE html>
<html lang="en">
<head>
<meta charset="utf-8">
<title>Estimate – Firmstone Paving</title>
<link href="https://fonts.googleapis.com/css2?family=Open+Sans:wght@400;600;700;800&display=swap" rel="stylesheet">
<style>
  :root {
    --backdrop: #e4e4e8;
    --paper: #ffffff;
    --navy: #33313f;
    --brick: #d3472c;
    --taupe: #8f857c;
    --ink: #222127;
    --rule: #b9b4ae;
  }
  * { box-sizing: border-box; margin: 0; padding: 0; }
  html, body {
    width: 1200px; height: 800px; overflow: hidden;
    background: var(--backdrop);
    font-family: "Open Sans", sans-serif;
    color: var(--ink);
  }
  .estimate {
    position: absolute; left: 320px; top: 10px;
    width: 560px; height: 780px;
    background: var(--paper);
    box-shadow: 0 6px 24px rgba(0,0,0,.18);
    overflow: hidden;
  }
  .brand {
    position: absolute; left: 26px; top: 26px;
    font-weight: 800; font-size: 18px; letter-spacing: 1px;
    line-height: 24px; white-space: nowrap;
    color: var(--navy); text-transform: uppercase;
  }
  .recipient-band {
    position: absolute; right: 0; top: 0; width: 290px; height: 74px;
    background: var(--navy);
    clip-path: polygon(0 0, 100% 0, 100% 100%, 32px 100%);
    color: #fff; text-align: right;
    padding: 4px 38px 0 0;
    font-size: 10.5px; line-height: 17px;
  }
  .project {
    position: absolute; left: 0; right: 0; top: 118px;
    text-align: center;
  }
  .project-title { font-size: 17px; font-weight: 600; }
  .project-address { font-size: 17px; margin-top: 8px; }
  .bid-number { font-size: 17px; margin-top: 20px; }
  .line-items {
    position: absolute; left: 46px; top: 294px; width: 471px;
    border-collapse: separate; border-spacing: 0;
    font-size: 9px; table-layout: fixed;
  }
  .line-items th {
    height: 41px; vertical-align: bottom; padding-bottom: 6px;
    font-weight: 700; font-size: 10px;
  }
  .line-items th.col-item {
    text-align: left; padding-left: 6px;
    border-top: 1px solid var(--rule);
    border-bottom: 1.5px solid var(--taupe);
  }
  .line-items th.col-num {
    background: var(--brick); color: #fff; text-align: center;
    border-left: 4px solid var(--paper); vertical-align: middle; padding: 0;
    line-height: 12px;
  }
  .line-items td {
    vertical-align: top; padding: 8px 6px 4px;
    border-bottom: 1px solid var(--rule);
    line-height: 13px;
  }
  .line-items td.num { text-align: center; padding-left: 2px; padding-right: 2px; }
  .line-items td.amount { text-align: right; font-weight: 700; padding-right: 4px; padding-left: 2px; white-space: nowrap; }
  .line-items tr.total-row td { border-bottom: 1px solid var(--rule); font-weight: 700; height: 28px; white-space: nowrap; }
  .line-items tr.spacer td { height: 26px; border-bottom: 1px solid #e2dfdb; }
  .footer-swoosh { position: absolute; left: 0; bottom: 0; width: 560px; height: 90px; }
</style>
</head>
<body>
  <main class="estimate">
    <div class="brand">Firmstone Paving</div>
    <div class="recipient-band">
      To:<br>
      Dana Whitfield<br>
      482 Harbor Lane SE Riverton 34190<br>
      dwhitfield@mailbox.example
    </div>

    <header class="project">
      <h1 class="project-title">Dana Whitfield New Concrete Pad</h1>
      <p class="project-address">482 Harbor Lane SE Riverton 34190</p>
      <p class="bid-number">Bid#: 20-0182</p>
    </header>

    <table class="line-items">
      <colgroup>
        <col style="width:281px"><col style="width:50px"><col style="width:38px"><col style="width:44px"><col style="width:58px">
      </colgroup>
      <thead>
        <tr>
          <th class="col-item">Item</th>
          <th class="col-num">Quantity</th>
          <th class="col-num">U/M</th>
          <th class="col-num">Unit<br>$</th>
          <th class="col-num">Total $</th>
        </tr>
      </thead>
      <tbody>
        <tr>
          <td>Form, Pour &amp; Finish New Concrete Slab (24' x 24' x 4"). Includes: 3000psi Concrete Mix, Footer (12" x 8") with One (#5) Continuous Rebar, Wire Mesh Reinforcement and Saw-Cut Expansion Joints</td>
          <td class="num">576</td>
          <td class="num">SF</td>
          <td class="num">$8.65</td>
          <td class="amount">$4,982.40</td>
        </tr>
        <tr>
          <td>OPTIONAL: Add (2' x 24' x 4") Small Ramp Area</td>
          <td class="num">48</td>
          <td class="num">SF</td>
          <td class="num">$8.65</td>
          <td class="amount">$415.20</td>
        </tr>
        <tr class="total-row">
          <td></td>
          <td colspan="3" style="text-align:right">Total Price</td>
          <td class="amount">$5,397.60</td>
        </tr>
        <tr class="spacer"><td colspan="5"></td></tr>
      </tbody>
    </table>

    <svg class="footer-swoosh" viewBox="0 0 560 90" aria-hidden="true">
      <path d="M0 90 L0 70 Q200 20 560 22 L560 90 Z" fill="var(--brick)"/>
      <path d="M0 58 Q180 12 460 10" fill="none" stroke="var(--navy)" stroke-width="3"/>
      <path d="M0 52 Q170 6 460 4" fill="none" stroke="var(--taupe)" stroke-width="2.5"/>
    </svg>
  </main>
</body>
</html>
```